Info-Flyer-Design für Inserate eines Katalogs von Papeterie- und Bürobedarf
Zielgruppe
FELDMARO ist ein Schweizer Grosshandelsunternehmen für Papeterie- und Bürobedarf. Kunden sind ausschliesslich professionelle Wiederverkäufer. Endverbraucher werden nicht direkt, sondern über FELDMARO Kunden beliefert.
Das Sortiment umfasst neben Papeterie- und Schulartikeln eine kompetente Auswahl im Bereich Bürobedarf. Die Produktepalette wird laufend weiterentwickelt und umfasst auch den Bereich Catering & Kaffee, Hygiene & Reinigung sowie Betriebssicherheit – alles was im modernen Büro benötigt wird.
FELDMARO bietet seinen Kunden umfassende Dienstleistungen an. Diese ermöglichen es, das vom Markt geforderte breite und tiefe Sortiment zielgruppengerecht erfolgreich zu vermarkten und effizient zu verteilen. In enger Zusammenarbeit mit unseren Kunden und Lieferanten entwickeln wir unsere Dienstleistungen stetig weiter. Neben den Vermarktungszielen stehen Effizienzziele, die Doppelspurigkeiten in der Wertschöpfungskette vermeiden, im Vordergrund.
Das oberste Ziel von FELDMARO ist es, ein zuverlässiger Partner zu sein. Deshalb geniessen Servicegrad und Lieferqualität höchste Priorität. Wir streben nach kooperativen und langfristigen Geschäftsbeziehungen und setzen neue Technologien zum gemeinsamen Nutzen ein.
Aufgabenstellung
In diesem Auftrag geht es darum, dass wir unseren Lieferanten ein Info Flyer zu senden, damit Sie Inserate in unserem nächsten Katalog für das Jahr 21/22 buchen. Es soll lebendig und erfrischend daher kommen. Das Format soll in A4 erstellt sein. Ich benötige am Ende die Original INDD Dokumente. Der Text kann gem. PDF Vorlage vom letzten Jahr übernommen werden, diesen werden wir selbstständig anpassen. Bitte das Logo in der Anlage verwenden sowie das Titelbild . Schrift haben wir ClanOT. Die Titelbalken (grün) haben wir immer so verwendet, da diese auch im Katalog erscheinen, hier kann aber auch die Farbe geändert werden.

```html
<!DOCTYPE html>
<html lang="de">
<head>
<meta charset="utf-8">
<title>FELDMARO Office 20/21 – Timetable</title>
<link rel="stylesheet" href="https://fonts.googleapis.com/css2?family=Fira+Sans+Condensed:wght@300;400;500;600&display=swap">
<style>
  :root {
    --backdrop: #adadad;
    --paper: #ffffff;
    --brand-yellow: #fecb32;
    --ink: #1e1e1e;
    --ink-soft: #333333;
    --rule-strong: #222222;
    --rule-light: #9a9a9a;
    --cell-highlight: #fdf7e5;
  }
  * { margin: 0; padding: 0; box-sizing: border-box; }
  html, body {
    width: 1200px; height: 848px; overflow: hidden;
    background: var(--backdrop);
    font-family: "Fira Sans Condensed", sans-serif;
    color: var(--ink);
  }
  .sheet {
    position: absolute; left: 22px; top: 20px;
    width: 570px; height: 804px;
    background: var(--paper);
  }
  .title-band {
    position: absolute; left: 29px; top: 30px;
    width: 511px; height: 53px;
    background: var(--brand-yellow);
  }
  .title-band__edition {
    position: absolute; left: 13px; top: 15px;
    font-size: 16px; font-weight: 500; color: var(--paper);
    letter-spacing: 0.2px;
  }
  .title-band__brand {
    position: absolute; right: 14px; top: 12px;
    font-size: 24px; font-weight: 600; color: var(--paper);
    letter-spacing: 1.5px; line-height: 1;
  }
  .section-title {
    position: absolute; left: 42px; top: 98px;
    font-size: 12.8px; font-weight: 600; letter-spacing: 0.3px;
  }
  .months {
    position: absolute; left: 72px; top: 159px;
    width: 454px; display: grid; grid-template-columns: repeat(6, 1fr);
    font-size: 11px; font-weight: 400;
  }
  .months span { padding-left: 4px; }
  .days {
    position: absolute; left: 40px; top: 186px;
    width: 26px;
  }
  .days span {
    display: flex; align-items: center; justify-content: center;
    height: 40.3px; font-size: 11px; font-weight: 400;
  }
  .timetable {
    position: absolute; left: 72px; top: 186px;
    width: 454px; height: 403px;
    border-top: 1.5px solid var(--rule-strong);
    border-left: 1.5px solid var(--rule-strong);
    display: grid;
    grid-template-columns: repeat(6, 1fr);
    grid-template-rows: repeat(10, 1fr);
  }
  .cell {
    border-right: 0.75px solid var(--rule-light);
    border-bottom: 0.75px solid var(--rule-light);
    padding: 9px 3px 0 4px;
    font-size: 9.6px; font-weight: 400; line-height: 1.1;
    color: var(--ink-soft);
  }
  .cell:nth-child(6n) { border-right: none; }
  .cell:nth-child(n+55) { border-bottom: none; }
  .cell--event { background: var(--cell-highlight); }
  .footnote {
    position: absolute; left: 42px; top: 736px;
    font-size: 10.6px; font-weight: 300; line-height: 1.5;
    color: var(--ink-soft);
  }
</style>
</head>
<body>
  <main class="sheet">
    <header class="title-band">
      <div class="title-band__edition">Office 20/21</div>
      <div class="title-band__brand">FELDMARO</div>
    </header>

    <h1 class="section-title">TIMETABLE</h1>

    <div class="months">
      <span>April</span><span>Mai</span><span>Juni</span><span>Juli</span><span>August</span><span>September</span>
    </div>

    <div class="days">
      <span>06</span><span>06</span><span>08</span><span>11</span><span>20</span>
      <span>22</span><span>25</span><span>27</span><span>29</span><span>31</span>
    </div>

    <div class="timetable">
      <!-- 06 -->
      <div class="cell cell--event">K1 Sortiment<br>Abgabe</div>
      <div class="cell"></div><div class="cell"></div>
      <div class="cell cell--event">K9 Sortiment<br>Abgabe</div>
      <div class="cell"></div><div class="cell"></div>
      <!-- 06 -->
      <div class="cell cell--event">Reservation<br>Imageseite</div>
      <div class="cell"></div><div class="cell"></div><div class="cell"></div><div class="cell"></div><div class="cell"></div>
      <!-- 08 -->
      <div class="cell"></div><div class="cell"></div>
      <div class="cell cell--event">K6 Sortiment<br>Abgabe</div>
      <div class="cell"></div><div class="cell"></div><div class="cell"></div>
      <!-- 11 -->
      <div class="cell"></div>
      <div class="cell cell--event">K4 Sortiment<br>Abgabe</div>
      <div class="cell"></div><div class="cell"></div><div class="cell"></div>
      <div class="cell cell--event">K9 Sortiment<br>Abgabe</div>
      <!-- 20 -->
      <div class="cell cell--event">K2 Sortiment<br>Abgabe</div>
      <div class="cell"></div><div class="cell"></div><div class="cell"></div><div class="cell"></div>
      <div class="cell cell--event">Abrechnung<br>Insertionskosten</div>
      <!-- 22 -->
      <div class="cell"></div><div class="cell"></div>
      <div class="cell cell--event">K7 Sortiment<br>Abgabe</div>
      <div class="cell"></div><div class="cell"></div><div class="cell"></div>
      <!-- 25 -->
      <div class="cell"></div>
      <div class="cell cell--event">K5 Sortiment<br>Abgabe</div>
      <div class="cell"></div><div class="cell"></div><div class="cell"></div><div class="cell"></div>
      <!-- 27 -->
      <div class="cell cell--event">K3 Sortiment<br>Abgabe</div>
      <div class="cell"></div><div class="cell"></div><div class="cell"></div><div class="cell"></div><div class="cell"></div>
      <!-- 29 -->
      <div class="cell"></div><div class="cell"></div>
      <div class="cell cell--event">K7 Sortiment<br>Abgabe</div>
      <div class="cell"></div><div class="cell"></div><div class="cell"></div>
      <!-- 31 -->
      <div class="cell"></div><div class="cell"></div><div class="cell"></div><div class="cell"></div>
      <div class="cell cell--event">Preisänderungen<br>an Feldmaro</div>
      <div class="cell"></div>
    </div>

    <p class="footnote">
      Die Gut zum Druck Phase wird von Ende Juli bis Mitte September 2018 in Etappen stattfinden,<br>
      wir werden Sie direkt per E-Mail informieren.
    </p>
  </main>
</body>
</html>
```